Powerpoint template for Trivia Company

Revamp of our current powerpoint template to make it more professional and fun for the players. Something worthy of a trivia company. Please see logo attached for potential colour - but also open to other ideas.

NO BRANDING REQUIRED (IE: No mention of our company or logo on the template please)

Target Market(s)

Bars/restaurants

Colors
3176b5
00a990

```html
<!DOCTYPE html>
<html lang="en">
<head>
<meta charset="utf-8">
<title>Trivia Night Presentation Template</title>
<link rel="stylesheet" href="https://fonts.googleapis.com/css2?family=Rubik:wght@800;900&family=Poppins:wght@500;600&family=Open+Sans:wght@400;600&family=Montserrat:wght@700&display=swap">
<style>
  :root {
    --blue: #3176b5;
    --teal: #00a990;
    --teal-pill: #1f9a9e;
    --ink: #111111;
    --text: #3c3c3c;
    --rule: #b9bcc0;
    --page: #dedede;
    --white: #ffffff;
  }
  * { box-sizing: border-box; margin: 0; padding: 0; }
  html, body { width: 1161px; height: 1200px; overflow: hidden; }
  body { background: var(--page); position: relative; font-family: "Poppins", sans-serif; }

  .slide { position: absolute; width: 357px; height: 203px; background: var(--white); overflow: hidden; }
  .col-1 { left: 23px; } .col-2 { left: 402px; } .col-3 { left: 782px; }
  .row-1 { top: 61px; } .row-2 { top: 284px; } .row-3 { top: 507px; } .row-4 { top: 729px; }

  .slide-title {
    position: absolute; left: 21px; top: 12px;
    font-family: "Rubik", sans-serif; font-weight: 900; font-size: 14px; color: var(--ink); letter-spacing: 0.2px;
  }
  .title-rule { position: absolute; left: 21px; top: 34px; width: 325px; height: 1px; background: var(--rule); }
  .title-rule::before { content: ""; position: absolute; left: 0; top: -0.5px; width: 39px; height: 2px; background: var(--teal-pill); }

  .footer-bar { position: absolute; left: 0; bottom: 0; width: 100%; height: 7px; display: flex; }
  .footer-bar span { flex: 1; }
  .footer-bar span:nth-child(odd) { background: var(--blue); }
  .footer-bar span:nth-child(even) { background: var(--teal); }

  .pill {
    position: absolute; height: 12px; padding: 0 8px; border-radius: 6px; background: var(--teal-pill);
    color: var(--white); font-family: "Poppins", sans-serif; font-weight: 500; font-size: 6.6px; line-height: 12px; white-space: nowrap;
  }
  .pill.centered { left: 50%; transform: translateX(-50%); }

  .welcome { background: linear-gradient(180deg, #05a98f 0%, #2491a6 45%, #3a72b6 100%); }
  .welcome h1 {
    position: absolute; left: 0; right: 0; top: 88px; text-align: center;
    font-family: "Rubik", sans-serif; font-weight: 900; font-size: 18px; color: var(--white); letter-spacing: 0.3px;
  }

  .rules-list {
    position: absolute; left: 34px; top: 59px; width: 294px; list-style: none;
    font-family: "Open Sans", sans-serif; font-size: 4.5px; line-height: 7.5px; color: #3a3a3a;
  }
  .rules-list li { position: relative; padding-left: 6px; margin-bottom: 3.8px; }
  .rules-list li::before { content: "•"; position: absolute; left: 0; }
  .rules-list b { font-weight: 600; }

  .question {
    position: absolute; left: 68px; right: 68px; top: 85px; text-align: center;
    font-family: "Poppins", sans-serif; font-weight: 500; font-size: 11px; line-height: 19px; color: var(--text);
  }

  .answer-list { position: absolute; left: 43px; top: 58px; list-style: none; font-family: "Open Sans", sans-serif; font-weight: 600; font-size: 7.2px; line-height: 12.2px; color: var(--ink); }
  .answer-list li { display: flex; }
  .answer-list .num { width: 22px; }

  .statement {
    position: absolute; left: 20px; right: 20px; top: 77px; text-align: center;
    font-family: "Poppins", sans-serif; font-weight: 500; font-size: 13.6px; line-height: 24px; color: var(--text);
  }
  .lead-in {
    position: absolute; left: 35px; top: 84px;
    font-family: "Poppins", sans-serif; font-weight: 500; font-size: 14px; line-height: 24.5px; color: var(--text);
  }

  .clue-list { position: absolute; left: 41px; top: 85px; width: 258px; list-style: none; font-family: "Poppins", sans-serif; font-weight: 500; font-size: 7.8px; line-height: 13.5px; color: var(--text); }
  .clue-list li { position: relative; padding-left: 12px; }
  .clue-list li::before { content: ""; position: absolute; left: 0; top: 5.5px; width: 2.5px; height: 2.5px; background: var(--text); }

  .logo-tile { position: absolute; width: 46px; height: 46px; background: var(--white); box-shadow: 0 1px 3px rgba(0,0,0,0.3); }
  .logo-tile .swatch { position: absolute; inset: 3px; }
  .tile-num { position: absolute; width: 46px; text-align: center; font-family: "Poppins", sans-serif; font-weight: 600; font-size: 6px; color: var(--ink); }

  .sign-off {
    position: absolute; left: 0; right: 0; top: 1019px; text-align: center;
    font-family: "Montserrat", sans-serif; font-weight: 700; font-size: 35px; letter-spacing: 13px; color: var(--ink); padding-left: 13px;
  }
</style>
</head>
<body>

  <section class="slide welcome col-1 row-1">
    <h1>Welcome to Trivia Night!</h1>
  </section>

  <section class="slide col-2 row-1">
    <h2 class="slide-title">The Rules</h2><div class="title-rule"></div>
    <ul class="rules-list">
      <li>Teams may have a maximum of <b>6</b> players.</li>
      <li>No outside help (internet, phone, etc.) of any kind, including during breaks! If you are caught, your team will be disqualified.</li>
      <li>The game is comprised of 7 rounds of 10 questions—each round is worth 20 points unless otherwise noted. At the end of each round, teams will exchange answer sheets to be graded. After 7 rounds, there will be a FINAL TRIVIA round where each team may wager up to 20 points on a single question.</li>
      <li>Before the game begins, each team must pick one BONUS category (excluding the Final Trivia round) for which they will be awarded double points.</li>
      <li>In the event of a tie, a tie-breaker question will decide the winner. In the unlikely event that the tied teams each answer the question correctly (closest), the winner shall be the team which hands the correct answer to the Quizmaster the quickest.</li>
      <li>The winning team (defined as 2 or more members on the same team, or 1 member if the winner was an individual) from the previous week shall be assessed a handicap equal to ½ of their winning margin (rounded down).</li>
      <li>The Quizmaster has final say on all rule interpretations and disputes.</li>
    </ul>
    <div class="footer-bar"><span></span><span></span><span></span><span></span></div>
  </section>

  <section class="slide col-3 row-1">
    <h2 class="slide-title">The Rules</h2><div class="title-rule"></div>
    <ul class="rules-list">
      <li>Teams may have a maximum of <b>6</b> players.</li>
      <li>No outside help (internet, phone, etc.) of any kind, including during breaks! If you are caught, your team will be disqualified.</li>
      <li>The game is comprised of 7 rounds of 10 questions—each round is worth 20 points unless otherwise noted. At the end of each round, teams will exchange answer sheets to be graded. After 7 rounds, there will be a FINAL TRIVIA round where each team may wager up to 20 points on a single question.</li>
      <li>Before the game begins, each team must pick one BONUS category (excluding the Final Trivia round) for which they will be awarded double points.</li>
      <li>In the event of a tie, a tie-breaker question will decide the winner. In the unlikely event that the tied teams each answer the question correctly (closest), the winner shall be the team which hands the correct answer to the Quizmaster the quickest.</li>
      <li>The winning team (defined as 2 or more members on the same team, or 1 member if the winner was an individual) from the previous week shall be assessed a handicap equal to ½ of their winning margin (rounded down).</li>
      <li>The Quizmaster has final say on all rule interpretations and disputes.</li>
    </ul>
    <div class="footer-bar"><span></span><span></span><span></span><span></span></div>
  </section>

  <section class="slide col-1 row-2">
    <h2 class="slide-title">General Knowledge</h2><div class="title-rule"></div>
    <div class="pill centered" style="top:62px">Question #1</div>
    <p class="question">What men’s evening wear got its name from a park in the Hudson Valley where New York’s elite were known to congregate in the 1890s?</p>
    <div class="footer-bar"><span></span><span></span><span></span><span></span></div>
  </section>

  <section class="slide col-2 row-2">
    <h2 class="slide-title">Answers:</h2><div class="title-rule"></div>
    <ol class="answer-list">
      <li><span class="num">1.</span>Tuxedo</li>
      <li><span class="num">2.</span>Surface to Air Missile</li>
      <li><span class="num">3.</span>Marisol (born in 1979)</li>
      <li><span class="num">4.</span>Edmund Harlow</li>
      <li><span class="num">5.</span>Nora Pembrook</li>
      <li><span class="num">6.</span>When Nature Calls</li>
      <li><span class="num">7.</span>Amira Sadeq</li>
      <li><span class="num">8.</span>The Riverton Herons</li>
      <li><span class="num">9.</span>Mercury</li>
      <li><span class="num">10.</span>Iceland</li>
    </ol>
    <div class="footer-bar"><span></span><span></span><span></span><span></span></div>
  </section>

  <section class="slide col-3 row-2">
    <h2 class="slide-title">One Word Movie Titles</h2><div class="title-rule"></div>
    <div class="pill centered" style="top:62px">Question #1</div>
    <p class="question">Which 2000 historical drama, directed by Elara Voss, follows Castor and his pursuit of revenge against the treacherous Regent Varro?</p>
    <div class="footer-bar"><span></span><span></span><span></span><span></span></div>
  </section>

  <section class="slide col-1 row-3">
    <h2 class="slide-title">Answers:</h2><div class="title-rule"></div>
    <ol class="answer-list">
      <li><span class="num">1.</span>Sentinel</li>
      <li><span class="num">2.</span>Mirage</li>
      <li><span class="num">3.</span>Leap</li>
      <li><span class="num">4.</span>Spiral</li>
      <li><span class="num">5.</span>Willow</li>
      <li><span class="num">6.</span>Tempest</li>
      <li><span class="num">7.</span>Drifter</li>
      <li><span class="num">8.</span>Outlaws</li>
      <li><span class="num">9.</span>Ember</li>
      <li><span class="num">10.</span>Lantern</li>
    </ol>
    <div class="footer-bar"><span></span><span></span><span></span><span></span></div>
  </section>

  <section class="slide col-2 row-3">
    <p class="statement">Please pass your answers to a<br>neighboring team</p>
    <div class="footer-bar"><span></span><span></span><span></span><span></span></div>
  </section>

  <section class="slide col-3 row-3">
    <div class="pill" style="left:32px;top:64px">Next Category</div>
    <p class="lead-in" style="top:84px">Name that Year – 2001-2010 Edition<br>(Each Year is Represented)</p>
  </section>

  <section class="slide col-1 row-4">
    <h2 class="slide-title">Name that year – 2001 - 2010</h2><div class="title-rule"></div>
    <div class="pill" style="left:23px;top:64px">Question #1</div>
    <ul class="clue-list">
      <li>Iran opens its first space center and launches a rocket into space</li>
      <li>Global financial crisis – President Warren Hale signs the revised Emergency Economic Stabilization Act into law</li>
      <li>Julian Crane dies</li>
    </ul>
    <div class="footer-bar"><span></span><span></span><span></span><span></span></div>
  </section>

  <section class="slide col-2 row-4">
    <div class="pill" style="left:32px;top:65px">Picture Round</div>
    <p class="lead-in" style="top:85px">One Letter Logos –<br>Name the Brand/Company</p>
    <div class="footer-bar"><span></span><span></span><span></span><span></span></div>
  </section>

  <section class="slide col-3 row-4">
    <div class="logo-tile" style="left:49px;top:48px"><div class="swatch" role="img" aria-label="Brand logo 1, red letter mark on white" style="background:#e4313a"></div></div>
    <div class="logo-tile" style="left:102px;top:48px"><div class="swatch" role="img" aria-label="Brand logo 2, coral letter mark on white" style="background:#ee6a6a"></div></div>
    <div class="logo-tile" style="left:155px;top:48px"><div class="swatch" role="img" aria-label="Brand logo 3, red letter mark" style="background:#e8262d"></div></div>
    <div class="logo-tile" style="left:208px;top:48px"><div class="swatch" role="img" aria-label="Brand logo 4, red sphere mark" style="background:#d8262f"></div></div>
    <div class="logo-tile" style="left:264px;top:48px"><div class="swatch" role="img" aria-label="Brand logo 5, red circle mark" style="background:#cf1f2b"></div></div>
    <div class="tile-num" style="left:49px;top:98px">1</div>
    <div class="tile-num" style="left:102px;top:98px">2</div>
    <div class="tile-num" style="left:155px;top:98px">3</div>
    <div class="tile-num" style="left:208px;top:98px">4</div>
    <div class="tile-num" style="left:264px;top:98px">5</div>
    <div class="logo-tile" style="left:49px;top:115px"><div class="swatch" role="img" aria-label="Brand logo 6, black letter mark on white" style="background:#1a1a1a"></div></div>
    <div class="logo-tile" style="left:102px;top:115px"><div class="swatch" role="img" aria-label="Brand logo 7, letter mark on yellow" style="background:#f6ac12"></div></div>
    <div class="logo-tile" style="left:155px;top:115px"><div class="swatch" role="img" aria-label="Brand logo 8, white letter on blue circle" style="background:#2b63c0"></div></div>
    <div class="logo-tile" style="left:208px;top:115px"><div class="swatch" role="img" aria-label="Brand logo 9, white letter on black" style="background:#1c1c1c"></div></div>
    <div class="logo-tile" style="left:264px;top:115px"><div class="swatch" role="img" aria-label="Brand logo 10, white letter on red" style="background:#e41b2c"></div></div>
    <div class="tile-num" style="left:49px;top:165px">6</div>
    <div class="tile-num" style="left:102px;top:165px">7</div>
    <div class="tile-num" style="left:155px;top:165px">8</div>
    <div class="tile-num" style="left:208px;top:165px">9</div>
    <div class="tile-num" style="left:264px;top:165px">10</div>
    <div class="footer-bar"><span></span><span></span><span></span><span></span></div>
  </section>

  <p class="sign-off">THANKS FOR WATCHING</p>

</body>
</html>
```